Create Print and Packaging Designs for an electric pepper mill grinder that will be sold as a set (2 grinders) (including package inserts). I have not selected the final product for the grinder yet, but I should have a decision made by the end of this week. In the images I'm attaching are samples of other very similar products and their current package designs (they're not my products). I really like the black ones and was thinking something similar. I am also attaching an image of my logo so you can use it in your submission. I know this is a bit more involved and I don't have all the details as of right now, but feel free to create artistically as you wish and ask for any clarification, and I will do my best to make decisions at that time. I would like something simple and elegant since that is the image I want for this brand. Also, I attached an image of the template of the product's box with dimensions.

```html
<!DOCTYPE html>
<html lang="en">
<head>
<meta charset="utf-8">
<title>Electric Pepper Mill Grinder – Packaging Panels</title>
<link rel="stylesheet" href="https://fonts.googleapis.com/css2?family=Open+Sans:wght@400;600&display=swap">
<style>
  :root {
    --bg: #eef0f1;
    --panel: #0b0b0c;
    --green: #8cc63f;
    --green-deep: #5e9a1c;
    --white: #ffffff;
    --grey-text: #c9cbcc;
    --steel-light: #d9dcde;
    --steel-dark: #6f7478;
  }
  * { box-sizing: border-box; margin: 0; padding: 0; }
  html, body { width: 1200px; height: 720px; overflow: hidden; }
  body {
    background: var(--bg);
    font-family: "Open Sans", Arial, sans-serif;
    color: var(--white);
    position: relative;
  }
  .panel {
    position: absolute;
    background: var(--panel);
    overflow: hidden;
  }
  .panel svg.bands { position: absolute; inset: 0; }

  /* brand lockup */
  .brand { position: absolute; display: flex; align-items: center; gap: 8px; }
  .brand-dot {
    width: 22px; height: 22px; border-radius: 50%;
    border: 2px solid var(--green);
  }
  .brand-name { font-size: 18px; font-weight: 400; color: var(--green); letter-spacing: 0.5px; }
  .brand-tagline {
    position: absolute; font-size: 8px; color: var(--green); letter-spacing: 0.4px;
  }

  .product-photo {
    position: absolute;
    background: linear-gradient(90deg, var(--steel-dark) 0%, var(--steel-light) 35%, #f4f5f6 50%, var(--steel-light) 65%, var(--steel-dark) 100%);
    border-radius: 6px 6px 4px 4px;
  }

  /* front panel */
  .front { left: 455px; top: 90px; width: 300px; height: 540px; }
  .front .brand { left: 92px; top: 22px; }
  .front .brand-tagline { left: 122px; top: 46px; }
  .front .title {
    position: absolute; top: 72px; left: 0; width: 100%;
    text-align: center; font-size: 27px; line-height: 1.18; font-weight: 400;
  }
  .front .product-photo { left: 118px; top: 170px; width: 64px; height: 330px; }

  /* side panel */
  .side { left: 150px; top: 90px; width: 280px; height: 540px; }
  .side .logo-ring {
    position: absolute; left: 30px; top: 24px; width: 60px; height: 60px;
    border-radius: 50%; border: 2px solid var(--green);
    display: flex; align-items: center; justify-content: center;
    font-size: 11px; color: var(--green);
  }
  .side .product-photo { left: 30px; top: 130px; width: 52px; height: 300px; }
  .side .features { position: absolute; left: 120px; top: 130px; width: 110px; }
  .feature { display: flex; flex-direction: column; align-items: center; margin-bottom: 22px; }
  .feature-icon {
    width: 62px; height: 62px;
    clip-path: polygon(25% 4%, 75% 4%, 100% 50%, 75% 96%, 25% 96%, 0 50%);
    background: radial-gradient(circle, #9ea3a6 0%, #3a3d40 60%, #d8dadc 100%);
  }
  .feature-label {
    margin-top: 6px; font-size: 10px; color: var(--grey-text); text-align: center; line-height: 1.3;
  }

  /* top panel */
  .top { left: 780px; top: 250px; width: 300px; height: 220px; }
  .top .product-photo {
    left: 40px; top: 18px; width: 190px; height: 44px; border-radius: 4px;
    background: linear-gradient(180deg, var(--steel-dark) 0%, var(--steel-light) 40%, #f4f5f6 55%, var(--steel-dark) 100%);
  }
  .top .seal {
    position: absolute; left: 170px; top: 92px; width: 96px; height: 96px;
    border-radius: 50%; background: var(--green);
    display: flex; align-items: center; justify-content: center;
    font-size: 15px; color: var(--white);
  }
</style>
</head>
<body>

  <!-- side panel: feature overview -->
  <section class="panel side">
    <svg class="bands" width="280" height="540" viewBox="0 0 280 540">
      <path d="M280,0 H252 Q236,270 252,540 H280 Z" fill="var(--green)"/>
      <path d="M246,0 Q230,270 246,540" fill="none" stroke="var(--white)" stroke-width="2"/>
    </svg>
    <div class="logo-ring">Marlowe</div>
    <div class="product-photo" role="img" aria-label="Exploded view of the stainless steel grinder parts"></div>
    <div class="features">
      <div class="feature">
        <div class="feature-icon" role="img" aria-label="Close-up of the power button"></div>
        <p class="feature-label">Power Button</p>
      </div>
      <div class="feature">
        <div class="feature-icon" role="img" aria-label="Close-up of the battery compartment"></div>
        <p class="feature-label">6 AAA Batteries<br>(Not Included)</p>
      </div>
      <div class="feature">
        <div class="feature-icon" role="img" aria-label="Close-up of the LED light"></div>
        <p class="feature-label">LED Light</p>
      </div>
    </div>
  </section>

  <!-- front panel -->
  <section class="panel front">
    <svg class="bands" width="300" height="540" viewBox="0 0 300 540">
      <path d="M0,0 H24 Q70,270 24,540 H0 Z" fill="var(--green)"/>
      <path d="M32,0 Q78,270 32,540" fill="none" stroke="var(--white)" stroke-width="2"/>
      <path d="M300,0 H276 Q230,270 276,540 H300 Z" fill="var(--green)"/>
      <path d="M268,0 Q222,270 268,540" fill="none" stroke="var(--white)" stroke-width="2"/>
    </svg>
    <div class="brand"><span class="brand-dot"></span><span class="brand-name">Marlowe</span></div>
    <p class="brand-tagline">Kitchen &amp; Dining Products</p>
    <h1 class="title">Electric Pepper<br>Mill Grinder</h1>
    <div class="product-photo" role="img" aria-label="Stainless steel electric pepper mill standing upright"></div>
  </section>

  <!-- top panel -->
  <section class="panel top">
    <svg class="bands" width="300" height="220" viewBox="0 0 300 220">
      <path d="M0,0 H110 Q60,30 0,50 Z" fill="var(--green)"/>
      <path d="M300,0 H190 Q240,30 300,50 Z" fill="var(--green)"/>
    </svg>
    <div class="product-photo" role="img" aria-label="Pepper mill lying on its side"></div>
    <div class="seal">Marlowe</div>
  </section>

</body>
</html>
```